**** Web design project for VornaSoft ****

For my ICT company VornaSoft I need a website.

We design, build and host web-applications and we have our own CMS product. In the references part we want to show sample websites (thumbnails) + links.

It should look modern (WEB 2.0), rounded corners.

I want the following menu' s:
- Home
- Services
- References
- News
- About VornaSoft
- Contact

Sample websites:
See attachments
http://www.plumvest.com
http://www.gadomirbureauwerk.nl

Reason: Want to take some time for feedback and improvements.

Reason: I'm waiting for a black background, with shadow and ambient light. You'll make a good chance!

Industry/Entity Type

It Company

Requirements
Must have
• - Fixed width (1024px), should fit on an IPad2
- Language selection English/Dutch
- social link 1/social link 3/social link 2/RSS icons
- Footer for Terms of use and Copyrights
- Search box
- 3 (or more) boxes for information i.e. news, blog or advertisements
Nice to have
• - Footer Site Map
- Contrasting background outside borders
- wide image (rotator) (with transperant sentence block)
- Shadow

```html
<!DOCTYPE html>
<html lang="en">
<head>
<meta charset="utf-8">
<title>VornaSoft</title>
<link href="https://fonts.googleapis.com/css2?family=Cabin:wght@400;500;600&family=Arimo:wght@400;700&display=swap" rel="stylesheet">
<style>
:root{
  --ink:#1a1a1a;
  --cyan:#27b4ea;
  --blue:#1a8fd0;
  --white:#ffffff;
  --rss:#f08a24;
}
*{margin:0;padding:0;box-sizing:border-box}
html,body{width:1015px;height:1200px;overflow:hidden;background:var(--white);font-family:"Arimo",sans-serif}
.page{position:relative;width:1015px;height:1200px;overflow:hidden;background:var(--white)}
.abs{position:absolute}
.topline{left:0;top:0;width:1015px;height:4px;background:var(--ink)}
.brand{left:96px;top:34px;display:flex;align-items:center;gap:12px}
.brand-dot{width:56px;height:56px;border-radius:50%;background:var(--blue)}
.brand-name{font-family:"Cabin",sans-serif;font-size:34px;font-weight:400;color:#5c6a73}
.lang{left:590px;top:22px;font-family:"Cabin",sans-serif;font-size:12px;color:#777;letter-spacing:.5px}
.lang b{color:var(--blue);font-weight:600}
.callbox{left:700px;top:4px;width:205px;height:58px;background:var(--ink);border-radius:0 0 12px 12px;color:var(--white)}
.callbox svg{position:absolute;left:14px;top:8px}
.call-label{position:absolute;left:84px;top:12px;font-size:17px;color:var(--cyan);letter-spacing:1px}
.call-num{position:absolute;left:72px;top:34px;font-size:16px;letter-spacing:1px}
.hero{left:0;top:129px;width:1015px;height:378px;background:radial-gradient(ellipse at 30% 40%,#333 0%,#222 50%,#181818 100%)}
.nav{left:92px;top:105px;width:825px;height:47px;border-radius:10px;background:linear-gradient(#fdfdfd,#d8d8d8);box-shadow:0 1px 3px rgba(0,0,0,.4);display:flex;align-items:center;overflow:hidden}
.nav a{font-family:"Cabin",sans-serif;font-size:13px;color:#333;text-decoration:none;padding:0 17px;height:20px;line-height:20px;border-right:1px solid #bbb;letter-spacing:.3px;white-space:nowrap}
.nav a.active{background:linear-gradient(#555,#2a2a2a);color:var(--white);height:47px;line-height:47px;padding:0 25px;border:0}
.nav a.last{border:0}
.search{margin-left:auto;margin-right:12px;width:160px;height:26px;border-radius:13px;background:var(--white);border:1px solid #bbb;box-shadow:inset 0 1px 2px rgba(0,0,0,.15);position:relative;font-size:11.5px;color:#999;line-height:24px;padding-left:11px}
.search svg{position:absolute;right:8px;top:5px}
.headline{left:88px;top:186px;font-family:"Cabin",sans-serif;font-size:40px;color:var(--white);font-weight:400}
.headline em{font-style:normal;color:var(--cyan);font-weight:500}
.subline{left:93px;top:244px;font-family:"Cabin",sans-serif;font-size:35px;color:var(--white);font-weight:400}
.intro{left:97px;top:300px;width:372px;font-size:11.5px;line-height:18.5px;color:#eee}
.cta{left:102px;top:434px;width:313px;height:34px;border-radius:10px;background:linear-gradient(#f2f2f2,#bdbdbd);font-family:"Cabin",sans-serif;font-size:12.5px;color:#222;line-height:34px;padding-left:7px;box-shadow:0 1px 3px rgba(0,0,0,.6)}
.cta b{position:absolute;right:7px;top:0;font-size:16px;color:#444}
.tablet{left:597px;top:173px;width:316px;height:407px;border-radius:18px;background:linear-gradient(#3a3a3a,#050505);border:3px solid #d0d0d0;box-shadow:0 12px 20px rgba(0,0,0,.35)}
.screen{left:34px;top:36px;width:249px;height:329px;background:linear-gradient(160deg,#0a0f1a 0%,#1b3350 45%,#8fb3d6 70%,#e85a1a 100%)}
.screen p{position:absolute;left:0;top:4px;font-family:"Cabin",sans-serif;font-size:20px;font-weight:500;color:var(--white);line-height:27px}
.dots{left:122px;top:376px;display:flex;gap:4px}
.dots i{width:10px;height:10px;border-radius:50%;background:#666}
.dots i.on{background:#ddd}
.who{left:82px;top:564px;font-family:"Cabin",sans-serif;font-size:20px;color:#444}
.clients{left:80px;top:612px;width:852px;height:62px;display:flex;justify-content:space-between;align-items:center}
.clients span{font-family:"Cabin",sans-serif;font-weight:600;font-size:22px;color:#7a7a7a}
.card{top:704px;width:253px;height:242px;border:1px solid #cfcfcf;border-radius:9px;background:var(--white);box-shadow:0 2px 4px rgba(0,0,0,.12);overflow:hidden}
.card h3{height:37px;background:linear-gradient(#3a3a3a,#151515);font-family:"Cabin",sans-serif;font-weight:400;font-size:20px;color:var(--white);line-height:38px;padding-left:14px}
.card .icon{position:absolute;right:6px;top:0;width:60px;height:40px;border-radius:6px}
.card .pic{position:absolute;left:13px;top:57px;width:223px;height:74px;border:1px solid #ddd}
.card p{position:absolute;left:13px;top:135px;width:224px;font-size:11px;line-height:15px;color:#444;letter-spacing:.3px;text-align:justify}
.card .more{position:absolute;left:15px;top:203px;width:73px;height:22px;border-radius:3px;background:linear-gradient(#3ec3f4,#1a8fd0);color:var(--white);font-size:11.5px;line-height:22px;text-align:center}
.card .demo{position:absolute;right:0;bottom:0}
.footer{left:0;top:976px;width:1015px;height:224px;background:radial-gradient(ellipse at 50% 30%,#2d2d2d,#141414)}
.footer h4{position:absolute;top:20px;font-family:"Cabin",sans-serif;font-weight:400;font-size:24px;color:var(--white);letter-spacing:.8px;padding-bottom:2px;border-bottom:1px dotted #555}
.footer .sep{position:absolute;top:14px;width:1px;height:200px;background:#333}
.links{position:absolute;left:110px;top:71px;list-style:none}
.links li{font-size:13.5px;color:var(--white);line-height:22px;letter-spacing:.4px;position:relative}
.links li::before{content:"";position:absolute;left:-17px;top:8px;border:4px solid transparent;border-left:5px solid var(--cyan)}
.profile{position:absolute;left:379px;top:70px;width:230px;font-size:11px;color:#9a9a9a;line-height:15px;letter-spacing:.8px}
.profile b{color:var(--cyan);font-size:12px}
.profile ul{list-style:none;margin-top:14px}
.profile li{color:#ddd;line-height:22px}
.social{position:absolute;left:716px;top:62px;display:flex;gap:9px}
.social i{width:38px;height:38px;border-radius:50%;background:radial-gradient(circle at 40% 35%,#7fd0f5,#1b7fc0);border:3px solid #e5e5e5;position:relative}
.social i.rss{background:radial-gradient(circle at 40% 35%,#ffb35c,var(--rss))}
.social i.rss svg{position:absolute;left:8px;top:8px}
.follow{position:absolute;left:717px;top:112px;width:240px;font-size:11px;color:#999;line-height:15px;letter-spacing:.6px}
.follow p+p{margin-top:12px}
</style>
</head>
<body>
<div class="page">
  <div class="abs topline"></div>
  <div class="abs brand"><span class="brand-dot"></span><span class="brand-name">VornaSoft</span></div>
  <div class="abs lang"><b>EN</b> | NL</div>
  <div class="abs callbox">
    <svg width="52" height="46" viewBox="0 0 52 46" aria-hidden="true">
      <rect x="4" y="6" width="20" height="32" rx="3" fill="#ddd"/>
      <rect x="7" y="10" width="14" height="22" fill="#333"/>
      <path d="M22 38 Q40 30 38 8" stroke="#27b4ea" stroke-width="5" fill="none"/>
      <path d="M31 10 L39 2 L46 11 Z" fill="#27b4ea"/>
    </svg>
    <span class="call-label">Call Now</span>
    <span class="call-num">1300 555 019</span>
  </div>
  <div class="abs hero"></div>
  <nav class="abs nav">
    <a class="active">HOME</a><a>SERVICES</a><a>REFERENCES</a><a>NEWS</a><a>ABOUT VORNASOFT</a><a class="last">CONTACT</a>
    <div class="search">Search...
      <svg width="14" height="14" viewBox="0 0 14 14" aria-hidden="true"><circle cx="6" cy="6" r="4.2" fill="none" stroke="#777" stroke-width="1.6"/><path d="M9 9 L13 13" stroke="#777" stroke-width="1.8"/></svg>
    </div>
  </nav>
  <h1 class="abs headline"><em>You’ve Got</em> The Traffic</h1>
  <h2 class="abs subline">Now Get The Sales.</h2>
  <p class="abs intro">Lorem Ipsum is simply dummy text of the printing and typesetting industry. Lorem Ipsum has been the industry's standard dummy text ever since the 1500s, when an unknown printer took a galley of type and scrambled it to make a type specimen book. It has survived not only five centuries, but also the leap into electronic typesetting, remaining essentially unchanged.</p>
  <div class="abs cta">Discover How You Can Increase Your Online Revenue <b>››</b></div>
  <div class="abs tablet">
    <div class="abs screen" role="img" aria-label="Slide image: rising orange arrow over blue bar graph">
      <p>Web Key Performance<br>Indicators</p>
    </div>
    <div class="abs dots"><i></i><i></i><i class="on"></i><i></i><i></i></div>
  </div>
  <div class="abs who">Who is using&nbsp; Tellivo to boost on-site conversion?</div>
  <div class="abs clients">
    <span>Kettlebay</span><span>Marlow Hire</span><span>Skyrundo</span><span>Drivana</span><span>Printwell</span><span>Orbank</span><span>Homeleaf</span>
  </div>

  <div class="abs card" style="left:85px">
    <h3>Web Development</h3>
    <div class="icon" role="img" aria-label="Illustration of figures holding letters" style="background:linear-gradient(#f0a020,#ddd)"></div>
    <div class="pic" role="img" aria-label="Photo of puzzle pieces with one golden piece" style="background:linear-gradient(90deg,#cfcfcf,#e8b020 70%,#bdbdbd)"></div>
    <p>LOREM IPSUM is simply dummy text of the printing and typesetting industry. Lorem Ipsum has been the industry's standard dummy.</p>
    <div class="more">Read more...</div>
    <svg class="demo" width="78" height="78" viewBox="0 0 78 78" aria-hidden="true"><path d="M78 0 V78 H0 Z" fill="#1d1d1d"/><text x="50" y="56" transform="rotate(-45 50 56)" fill="#fff" font-family="Arimo,sans-serif" font-size="10" font-weight="700" text-anchor="middle">DOWNLOAD</text><text x="58" y="64" transform="rotate(-45 58 64)" fill="#fff" font-family="Arimo,sans-serif" font-size="10" font-weight="700" text-anchor="middle">DEMO</text></svg>
  </div>

  <div class="abs card" style="left:369px">
    <h3 style="padding-left:40px">Traffic Generation</h3>
    <div class="icon" role="img" aria-label="Traffic light icon" style="width:40px;right:10px;background:linear-gradient(#222,#444)"></div>
    <div class="pic" role="img" aria-label="Photo of congested city traffic" style="background:linear-gradient(#8a8a8a,#b44 55%,#d9892f)"></div>
    <p>LOREM IPSUM is simply dummy text of the printing and typesetting industry. Lorem Ipsum has been the industry's standard dummy.</p>
    <div class="more">Read more...</div>
    <svg class="demo" width="78" height="78" viewBox="0 0 78 78" aria-hidden="true"><path d="M78 0 V78 H0 Z" fill="#1d1d1d"/><text x="50" y="56" transform="rotate(-45 50 56)" fill="#fff" font-family="Arimo,sans-serif" font-size="10" font-weight="700" text-anchor="middle">DOWNLOAD</text><text x="58" y="64" transform="rotate(-45 58 64)" fill="#fff" font-family="Arimo,sans-serif" font-size="10" font-weight="700" text-anchor="middle">DEMO</text></svg>
  </div>

  <div class="abs card" style="left:656px">
    <h3 style="padding-left:50px">Web Analytics</h3>
    <svg class="icon" width="56" height="44" viewBox="0 0 56 44" aria-hidden="true" style="right:2px"><circle cx="28" cy="22" r="18" fill="#e53a2a"/><path d="M28 22 V4 A18 18 0 0 1 46 22 Z" fill="#6cc83a"/><path d="M28 22 H46 A18 18 0 0 1 34 39 Z" fill="#f2c320"/></svg>
    <div class="pic" role="img" aria-label="Colourful 3D bar chart on a grid" style="background:linear-gradient(90deg,#f1f1f1,#f5a020 35%,#d23a8a 60%,#6a3ad0 75%,#3cc83a)"></div>
    <p>LOREM IPSUM is simply dummy text of the printing and typesetting industry. Lorem Ipsum has been the industry's standard dummy.</p>
    <div class="more">Read more...</div>
    <svg class="demo" width="78" height="78" viewBox="0 0 78 78" aria-hidden="true"><path d="M78 0 V78 H0 Z" fill="#1d1d1d"/><text x="50" y="56" transform="rotate(-45 50 56)" fill="#fff" font-family="Arimo,sans-serif" font-size="10" font-weight="700" text-anchor="middle">DOWNLOAD</text><text x="58" y="64" transform="rotate(-45 58 64)" fill="#fff" font-family="Arimo,sans-serif" font-size="10" font-weight="700" text-anchor="middle">DEMO</text></svg>
  </div>

  <footer class="abs footer">
    <h4 style="left:100px">Quick Links</h4>
    <ul class="links">
      <li>Home</li><li>Services</li><li>References</li><li>News</li><li>About VornaSoft</li><li>Contact</li>
    </ul>
    <div class="sep" style="left:318px"></div>
    <h4 style="left:384px">Company Profile</h4>
    <div class="profile">
      <b>Lorem Ipsum</b> is simply dummy text of the printing and typesetting industry and typesetting industry.
      <ul><li>* Suppliers of IT Hardware and Software</li><li>* Office IT Infrastructure Setup</li><li>* Remote and Onsite Support</li></ul>
    </div>
    <div class="sep" style="left:662px"></div>
    <h4 style="left:726px">Follow Us</h4>
    <div class="social">
      <i aria-label="Social link 1"></i><i aria-label="Social link 2"></i><i aria-label="Social link 3"></i>
      <i class="rss" aria-label="RSS feed"><svg width="16" height="16" viewBox="0 0 16 16" aria-hidden="true"><circle cx="3" cy="13" r="2" fill="#fff"/><path d="M1 7 A8 8 0 0 1 9 15" stroke="#fff" stroke-width="2.2" fill="none"/><path d="M1 2 A13 13 0 0 1 14 15" stroke="#fff" stroke-width="2.2" fill="none"/></svg></i>
    </div>
    <div class="follow">
      <p>Lorem Ipsum is simply dummy text of the printing and typesetting industry.</p>
      <p>Copyright 2011 Brightpane Studio.<br>Privacy Policy | Terms Of Service</p>
    </div>
  </footer>
</div>
</body>
</html>
```